Real Estate Investment Company Needs A Business Card Designed

I need a business card designed for my use. We are a real estate investment company based in Omaha, Nebraska that specializes in buying, rehabbing and selling single family and multifamily properties. Would love designs that incorporate our logo and colors

Industry/Entity Type

Business

Contact Information for Business Card

Marlow Pettigrew | President & CEO
4837 North 52nd Avenue, Ste 200
Omaha, NE 68214
(402) 555-7428
marlow@quillfenhomes.example
www.QuillfenHomes.example

Font styles to use
Serif

Colors
0255a3
3276b5

Requirements
Must have
• Our logo

```html
<!DOCTYPE html>
<html lang="en">
<head>
<meta charset="utf-8">
<title>Quillfen Homes — Business Card</title>
<link href="https://fonts.googleapis.com/css2?family=Open+Sans:wght@400;600;700&display=swap" rel="stylesheet">
<style>
  :root {
    --brand-blue: #0255a3;
    --brand-blue-light: #3276b5;
    --ink: #1e1e1e;
    --card-white: #f7f8fa;
    --card-black: #050505;
    --stage: #e9e6e1;
  }
  * { margin: 0; padding: 0; box-sizing: border-box; }
  html, body { width: 1200px; height: 800px; overflow: hidden; }
  body {
    background: var(--stage);
    font-family: "Open Sans", Arial, sans-serif;
    position: relative;
  }
  .card {
    position: absolute;
    top: 250px;
    width: 525px;
    height: 300px;
    border-radius: 3px;
    box-shadow: 0 6px 18px rgba(0,0,0,0.18);
    overflow: hidden;
  }
  /* Back of card */
  .card-back {
    left: 60px;
    background: var(--card-black);
    display: flex;
    align-items: center;
    justify-content: center;
  }
  .brand-lockup {
    display: flex;
    align-items: center;
    gap: 14px;
  }
  .brand-dot {
    width: 26px; height: 26px;
    border-radius: 50%;
    background: var(--brand-blue-light);
  }
  .brand-name {
    color: var(--brand-blue-light);
    font-weight: 700;
    font-size: 34px;
    letter-spacing: 1px;
    text-transform: uppercase;
  }
  /* Front of card */
  .card-front {
    left: 615px;
    background: var(--card-white);
  }
  .card-bands { position: absolute; inset: 0; }
  .holder {
    position: absolute;
    left: 30px; top: 40px;
  }
  .holder-name {
    color: var(--brand-blue);
    font-weight: 700;
    font-size: 21px;
    letter-spacing: 0.8px;
    text-transform: uppercase;
    line-height: 1.1;
  }
  .holder-title {
    color: var(--ink);
    font-size: 15px;
    line-height: 1.3;
  }
  .address {
    position: absolute;
    left: 30px; top: 112px;
    color: var(--ink);
    font-size: 13.5px;
    line-height: 1.35;
    font-style: normal;
  }
  .contacts {
    position: absolute;
    left: 20px; top: 178px;
    list-style: none;
    color: var(--ink);
    font-size: 13.5px;
  }
  .contacts li {
    display: flex;
    align-items: center;
    gap: 8px;
    height: 21px;
  }
  .contacts svg { width: 13px; height: 13px; flex: none; }
  .card-mark {
    position: absolute;
    right: 34px; top: 70px;
    width: 150px; height: 150px;
    border: 3px solid var(--brand-blue-light);
    border-radius: 50%;
    display: flex;
    align-items: center;
    justify-content: center;
    text-align: center;
  }
  .card-mark .brand-name {
    font-size: 19px;
    line-height: 1.2;
    color: var(--brand-blue-light);
  }
</style>
</head>
<body>

  <section class="card card-back" aria-label="Card back">
    <div class="brand-lockup">
      <span class="brand-dot"></span>
      <span class="brand-name">Quillfen Homes</span>
    </div>
  </section>

  <section class="card card-front" aria-label="Card front">
    <svg class="card-bands" viewBox="0 0 525 300" preserveAspectRatio="none" aria-hidden="true">
      <polygon points="0,0 300,0 280,16 0,16" fill="var(--brand-blue-light)"/>
      <polygon points="245,284 265,268 525,268 525,300 245,300" fill="var(--brand-blue-light)" transform="translate(0,0)"/>
    </svg>

    <header class="holder">
      <h1 class="holder-name">Marlow Pettigrew</h1>
      <p class="holder-title">President &amp; CEO</p>
    </header>

    <address class="address">
      4837 North 52nd Avenue, Ste 200<br>
      Omaha, NE 68214
    </address>

    <ul class="contacts">
      <li>
        <svg viewBox="0 0 16 16"><path d="M4 1l3 3-1.6 1.8c.8 1.9 2.2 3.3 4.1 4.1L11.3 8.3l3 3-1.6 2.5C7 13.6 2.4 9 2.2 3z" fill="var(--brand-blue)"/></svg>
        <span>(402) 555-7428</span>
      </li>
      <li>
        <svg viewBox="0 0 16 16"><rect x="1" y="3" width="14" height="10" fill="var(--brand-blue)"/><path d="M1 3l7 6 7-6" fill="none" stroke="#fff" stroke-width="1.2"/></svg>
        <span>marlow@quillfenhomes.example</span>
      </li>
      <li>
        <svg viewBox="0 0 16 16"><circle cx="8" cy="8" r="6.5" fill="none" stroke="var(--brand-blue)" stroke-width="1.5"/><ellipse cx="8" cy="8" rx="3" ry="6.5" fill="none" stroke="var(--brand-blue)" stroke-width="1.2"/><path d="M1.5 8h13M2.5 5h11M2.5 11h11" stroke="var(--brand-blue)" stroke-width="1"/></svg>
        <span>www.QuillfenHomes.example</span>
      </li>
    </ul>

    <div class="card-mark">
      <span class="brand-name">Quillfen<br>Homes</span>
    </div>
  </section>

</body>
</html>
```